Business card design for QuadVentura

I need a business card based on the logo design produced for QuadVentura. The company is focused on triathlon and endurance sport coaching and the tag line is (per the logo) "Endurance. Resilience. Achievement". The design should be sophisticated, appropriate to an affluent and business oriented target market. Colors are optional but the color of the logo probably dictates the color used on the card. I envisage using the red logo, with black print for the wording and contact numbers on a white or cream background, but am open to alternative suggestions. I expect to select something fairly conventional, but would like to see some designs that are less conventional to stretch my thinking on what could be appropriate. I am assuming a single side design is best, but willing to consider double sided as an option.

Target Market(s)

Individual athletes and corporate health and wellness leaders

Industry/Entity Type

Health And Wellness

Contact Information for Business Card

The card should provide the following information:
Logo
My name: Malcolm Ashgrove
Company website: QuadVentura.com
My email: malcolm.ashgrove@quadventura.com
My cell phone number: +1-555-814-2973

Font styles to use
Sans Serif

Colors

Designer to choose colors to be used in the design.

Requirements
Must have
• Space on the card - simple design, not over crowded.
Nice to have
• clean and clear font, nothing garish or mass market like
Should not have
• Do not add pictures

```html
<!DOCTYPE html>
<html lang="en">
<head>
<meta charset="utf-8">
<title>QuadVentura Business Card</title>
<link rel="stylesheet" href="https://fonts.googleapis.com/css2?family=Cabin:wght@400;500;600;700&display=swap">
<style>
  :root {
    --backdrop: #bdbdbd;
    --brand-red: #8b2624;
    --brand-red-deep: #7f2220;
    --card-white: #efefef;
    --ink: #222222;
    --stripe-dark: #3a3a3a;
    --on-red: #f4f0ee;
  }
  * { margin: 0; padding: 0; box-sizing: border-box; }
  html, body {
    width: 1200px;
    height: 576px;
    overflow: hidden;
    background: var(--backdrop);
    font-family: "Cabin", sans-serif;
  }
  .canvas { position: relative; width: 1200px; height: 576px; }

  .card {
    position: absolute;
    top: 138px;
    height: 293px;
    border-radius: 11px;
    overflow: hidden;
  }

  /* Front */
  .card-front {
    left: 82px;
    width: 484px;
    background: linear-gradient(180deg, var(--brand-red) 0%, var(--brand-red-deep) 100%);
    color: var(--on-red);
    text-align: center;
  }
  .card-front .brand-name {
    position: absolute;
    left: 0; right: 0;
    top: 136px;
    font-size: 42px;
    font-weight: 600;
    line-height: 1;
    letter-spacing: 0.2px;
  }

  /* Back */
  .card-back {
    left: 602px;
    width: 481px;
    background: var(--card-white);
  }
  .side-band {
    position: absolute;
    left: 0; top: 0; bottom: 0;
    width: 42px;
    background: var(--brand-red);
  }
  .side-stripe {
    position: absolute;
    left: 42px; top: 0; bottom: 0;
    width: 5px;
    background: var(--stripe-dark);
  }
  .back-brand {
    position: absolute;
    left: 68px;
    top: 64px;
    font-size: 32px;
    font-weight: 600;
    color: var(--brand-red);
    line-height: 1;
  }
  .person-name {
    position: absolute;
    left: 68px;
    top: 189px;
    font-size: 21px;
    font-weight: 700;
    color: var(--brand-red);
    letter-spacing: 0.3px;
  }
  .contact-list {
    position: absolute;
    left: 68px;
    top: 221px;
    list-style: none;
  }
  .contact-list li {
    display: flex;
    align-items: center;
    height: 18.5px;
    font-size: 12.5px;
    color: var(--ink);
  }
  .contact-list svg {
    width: 10px;
    height: 10px;
    margin-right: 8px;
    fill: var(--brand-red);
  }
  .contact-list .accent { color: var(--brand-red); }
</style>
</head>
<body>
<main class="canvas">

  <section class="card card-front" aria-label="Card front">
    <div class="brand-name">QuadVentura</div>
  </section>

  <section class="card card-back" aria-label="Card back">
    <div class="side-band"></div>
    <div class="side-stripe"></div>

    <div class="back-brand">QuadVentura</div>

    <div class="person-name">Malcolm Ashgrove</div>

    <ul class="contact-list">
      <li>
        <svg viewBox="0 0 10 10" aria-hidden="true"><path d="M1 3.2C1 2 2.5 1.2 5 1.2S9 2 9 3.2V4H7V3H3v1H1z M2.2 5h5.6L9 9H1z"/></svg>
        +1-555-814-2973
      </li>
      <li>
        <svg viewBox="0 0 10 10" aria-hidden="true"><path d="M0.5 2h9v6h-9z M0.5 2L5 5.5 9.5 2" stroke="#efefef" stroke-width="0.8"/></svg>
        malcolm.ashgrove@quadventura.com
      </li>
      <li>
        <svg viewBox="0 0 10 10" aria-hidden="true"><circle cx="5" cy="5" r="4.3"/><path d="M0.7 5h8.6M5 0.7v8.6M2 2.6h6M2 7.4h6" stroke="#efefef" stroke-width="0.6" fill="none"/></svg>
        <span>www.<span class="accent">QuadVentura</span>.com</span>
      </li>
    </ul>
  </section>

</main>
</body>
</html>
```